B2B Case Study Template Design (InDesign or Affinity Designer)

Hello,We are a company specializing in custom sanitary space fit-outs and Solid Surface manufacturing. We are looking for a talented layout designer to create a professional and modern "Case Study" template to showcase our projects.This template must strictly be designed using Adobe InDesign or Affinity Designer. We do not want Canva, Word, or PowerPoint files.Attached, there is a file you can reference named "Balu - Case Study.pdf". This is our previous layout.

Your mission is to recreate this case study using our new brand guidelines (which I will also provide) while using the exact same texts, photos, and sections (Key Data / "Données clés", Verlo's Role / "Le rôle d'Verlo", Verlo Products / "Produits Verlo").

Note: This project is the first of a series. We want to keep everything in the same project scope moving forward. If the work is satisfactory, we will hire you directly for upcoming print materials (flyer templates, catalogs, etc.).

---
2 Exemples of existing Case Studies : BALU and SOFT RIM
1 Full INDISIGN assembled file for DELORME project (you can work from there)
The logo (multi format)
And a zip file with the PATTERN, FONT and LOGO ALTERNATIVES (for graphic use only - on a photo, or else)

Target Market(s)

Building professionals, architects, specifiers, B2B companies, and contractors.

Industry/Entity Type

Architecture / Construction / B2B

Font styles to use
Sans Serif

Requirements
Must have
• The final source file must be delivered in Adobe InDesign (.indd/.idml) or Affinity Designer format. The design must be clean, structured, and highlight the architectural photography. Paragraph and character styles must be properly set up in the software so we can easily edit the text ourselves in the future. Strict integration of our new brand guidelines (colors, typography).
Nice to have
• A modular design: a layout that works perfectly for a 2-page (front/back) document, but can be easily expanded to 3 or 4 pages if a specific case study requires more content. Layout suggestions for recurring graphic elements (e.g., custom icons for key data, elegant frames for pull quotes).
Should not have
• Do NOT use Canva, Microsoft Word, or Photoshop for the layout. Avoid cluttered, overly colorful, or whimsical designs. We are looking for a premium, high-end, and serious aesthetic suited for the architectural field.

```html
<!DOCTYPE html>
<html lang="fr">
<head>
<meta charset="utf-8">
<title>Projet Delorme – Étude de cas</title>
<link href="https://fonts.googleapis.com/css2?family=Poppins:wght@300;400;500;600;700&family=Jost:wght@300;400;500;600;700&family=Oswald:wght@500;600&display=swap" rel="stylesheet">
<style>
  :root{
    --stage:#231f20;
    --frame-a:#e6ded0;
    --cream-a:#f2ebe0;
    --ink:#2b2925;
    --ink-soft:#5b5750;
    --rule:#b9b0a2;
    --frame-b:#efebe4;
    --paper-b:#faf8f3;
    --border-b:#d9d3c9;
    --taupe:#a79e91;
    --white:#ffffff;
  }
  *{box-sizing:border-box;margin:0;padding:0}
  html,body{width:1200px;height:1000px;overflow:hidden;background:var(--stage)}
  body{position:relative;font-family:'Poppins',sans-serif;color:var(--ink)}
  .abs{position:absolute}

  /* ---------- Spread A (Verlo) ---------- */
  .spread-a{position:absolute;left:271px;top:30px;width:658px;height:465px;background:var(--frame-a)}
  .page{position:absolute;overflow:hidden}
  .cover-a{left:13px;top:13px;width:309px;height:438px;box-shadow:0 1px 3px rgba(0,0,0,.12)}
  .photo{position:absolute}
  .photo-washroom{background:linear-gradient(180deg,#e4e2dc 0%,#5f6f47 12%,#56683f 44%,#dcd8d1 52%,#f7f7f5 60%,#9a6a3f 68%,#7d5231 92%,#b8ad9f 100%)}
  .photo-basin{background:linear-gradient(160deg,#f6f6f4 0%,#e9e9e7 55%,#cfcfcc 100%)}
  .photo-support{background:linear-gradient(180deg,#e7e2da 0%,#fbfbfa 40%,#f3f3f1 70%,#6e6e70 100%)}
  .photo-mirror{background:linear-gradient(135deg,#f1f1ef 0%,#c9c9c7 50%,#efefed 100%)}
  .sidebar-a{position:absolute;left:6px;top:0;width:75px;height:100%;background:var(--cream-a)}
  .brand-a{font-family:'Poppins',sans-serif;font-weight:700;font-size:13px;letter-spacing:-.2px;color:var(--ink)}
  .micro{font-size:3.6px;letter-spacing:1.4px;line-height:7px;text-transform:uppercase;color:var(--ink)}
  .hair{position:absolute;height:.6px;background:var(--ink-soft)}
  .cover-title-a{position:absolute;left:89px;top:295px;font-weight:700;font-size:20px;line-height:21px;color:var(--white)}
  .cover-sub-a{position:absolute;left:89px;top:351px;font-weight:600;font-size:10.6px;line-height:14px;color:var(--white)}

  .inner-a{left:335px;top:13px;width:311px;height:438px;background:var(--cream-a);box-shadow:0 1px 3px rgba(0,0,0,.12)}
  .head-a{font-size:3.6px;letter-spacing:1.3px;text-transform:uppercase;color:var(--ink-soft)}
  .title-a{position:absolute;left:15px;top:153px;font-weight:500;font-size:13.4px;line-height:15.5px;letter-spacing:-.1px;color:var(--ink)}
  .lead-a{position:absolute;left:15px;top:191px;width:272px;font-size:4.9px;line-height:7.3px;color:var(--ink)}
  .rule-a{position:absolute;left:15px;width:281px;height:.6px;background:var(--rule)}
  .h-a{font-weight:700;font-size:7.8px;letter-spacing:.1px;color:var(--ink)}
  .list-a{list-style:none;font-size:4.9px;line-height:10px}
  .list-a li{display:flex;align-items:center;gap:4px}
  .list-a svg{width:6px;height:6px;flex:none}
  .list-a b{font-weight:600}
  .product-a{position:absolute;top:308px;width:88px;height:61px}
  .product-label-a{position:absolute;top:377px;width:88px;text-align:center;font-weight:500;font-size:5px;line-height:6.6px;text-transform:uppercase}
  .foot-a{font-size:3.6px;letter-spacing:1.4px;line-height:6.5px;text-transform:uppercase;color:var(--ink-soft)}
  .foot-tags-a{font-size:2.8px;letter-spacing:1px;line-height:4px;text-transform:uppercase;color:var(--ink-soft)}

  /* ---------- Spread B (Norvi) ---------- */
  .spread-b{position:absolute;left:271px;top:505px;width:658px;height:465px;background:var(--frame-b);font-family:'Jost',sans-serif}
  .cover-b{left:6px;top:4px;width:320px;height:456px;background:var(--paper-b);border:.6px solid var(--border-b)}
  .inner-b{left:332px;top:4px;width:322px;height:456px;background:var(--paper-b);border:.6px solid var(--border-b)}
  .brand-b{font-family:'Jost',sans-serif;font-weight:500;color:var(--ink);text-transform:uppercase}
  .kicker-b{font-size:3.6px;letter-spacing:1.6px;text-transform:uppercase;color:var(--ink-soft)}
  .project-b{font-weight:300;font-size:11px;letter-spacing:2px;color:var(--ink)}
  .name-b{font-family:'Oswald',sans-serif;font-weight:600;font-size:24px;line-height:26px;letter-spacing:-.2px;color:var(--ink)}
  .sub-b{font-weight:400;font-size:7.2px;line-height:11px;color:var(--ink)}
  .title-b{position:absolute;left:17px;top:29px;font-size:14px;line-height:17.5px;font-weight:400;color:var(--ink)}
  .title-b strong{font-weight:600}
  .side-b{font-size:3.7px;letter-spacing:1.6px;line-height:9px;text-transform:uppercase;color:var(--ink-soft)}
  .tile-b{position:absolute;left:234px;top:189px;width:73px;height:85px;background:var(--taupe)}
  .tile-b p{position:absolute;left:9px;top:17px;font-size:3.8px;letter-spacing:1.5px;line-height:8.5px;text-transform:uppercase;color:var(--paper-b)}
  .h-b{font-weight:500;font-size:5.6px;letter-spacing:1.2px;text-transform:uppercase;color:var(--ink)}
  .short-rule{position:absolute;width:12px;height:.6px;background:var(--ink)}
  .vrule{position:absolute;width:.6px;background:var(--border-b)}
  .data-b{position:absolute;font-size:4.8px;line-height:6.6px;color:var(--ink)}
  .data-b b{font-weight:600}
  .role-b{position:absolute;display:flex;gap:4px;font-size:4.8px;line-height:7.2px;color:var(--ink)}
  .role-b::before{content:"";width:5px;height:.6px;background:var(--ink);margin-top:3.6px;flex:none}
  .swatch-b{position:absolute;left:226px;width:33px;height:33px;border-radius:50%}
  .swatch-label-b{position:absolute;left:266px;width:50px;font-size:3.6px;font-weight:400;letter-spacing:.5px;line-height:5px;text-transform:uppercase;color:var(--ink);white-space:nowrap}
</style>
</head>
<body>

<!-- ===== Spread A ===== -->
<section class="spread-a">
  <article class="page cover-a">
    <div class="photo photo-washroom" style="left:0;top:0;width:100%;height:100%" role="img" aria-label="Photo du bloc sanitaire rénové : mur vert, grand miroir, plan vasque blanc et meubles en bois"></div>
    <aside class="sidebar-a">
      <div class="abs brand-a" style="left:15px;top:17px">Verlo.</div>
      <p class="abs micro" style="left:15px;top:44px">Espaces<br>sanitaires<br>sur-mesure</p>
      <span class="hair" style="left:15px;top:72px;width:24px"></span>
      <p class="abs micro" style="left:15px;top:199px;font-size:3.4px">Établissements<br>qui avancent<br>avec vous</p>
      <span class="hair" style="left:15px;top:226px;width:24px"></span>
      <p class="abs micro" style="left:15px;top:412px;font-weight:600">verlo.fr</p>
    </aside>
    <h1 class="cover-title-a">PROJET<br>DELORME</h1>
    <span class="hair" style="left:89px;top:343px;width:30px;background:var(--white)"></span>
    <p class="cover-sub-a">L’ART DE L’AGILITÉ :<br>RÉNOVATION SANITAIRE<br>EN SITE OCCUPÉ</p>
  </article>

  <article class="page inner-a">
    <p class="abs head-a" style="left:15px;top:10px">Verlo &nbsp;|&nbsp; Projets</p>
    <p class="abs head-a" style="right:15px;top:10px">Espaces sanitaires sur-mesure</p>
    <div class="photo photo-washroom" style="left:15px;top:22px;width:281px;height:126px" role="img" aria-label="Photo du plan vasque double sous le miroir, mur vert et portes bois"></div>

    <h2 class="title-a">Projet Delorme : quand la performance<br>s’adapte à la continuité de service</h2>
    <p class="lead-a">Une rénovation sanitaire en site occupé qui conjugue exigence fonctionnelle, design épuré et parfaite maîtrise d’exécution. Grâce à des solutions sur-mesure et une organisation millimétrée, Verlo accompagne les établissements dans leurs projets de transformation, sans perturber leur activité.</p>
    <span class="rule-a" style="top:224px"></span>

    <h3 class="abs h-a" style="left:16px;top:231px">DONNÉES CLÉ</h3>
    <ul class="abs list-a" style="left:16px;top:244px">
      <li><svg viewBox="0 0 10 10"><path d="M5 9.5S1.8 6 1.8 3.9a3.2 3.2 0 0 1 6.4 0C8.2 6 5 9.5 5 9.5z" fill="none" stroke="#2b2925" stroke-width="1"/><circle cx="5" cy="3.9" r="1.1" fill="#2b2925"/></svg><span><b>Lieu :</b> 12 Avenue Delorme, Paris 17e</span></li>
      <li><svg viewBox="0 0 10 10"><rect x="1.5" y="1" width="5" height="8" fill="none" stroke="#2b2925"/><rect x="6.5" y="4" width="2.5" height="5" fill="none" stroke="#2b2925"/><path d="M3 3h2M3 5h2M3 7h2" stroke="#2b2925" stroke-width=".8"/></svg><span><b>Maître d’ouvrage :</b> Banque Astrelle</span></li>
      <li><svg viewBox="0 0 10 10"><rect x="2" y="1" width="6" height="8" fill="none" stroke="#2b2925"/><path d="M3.5 3.5h3M3.5 5h3M3.5 6.5h3" stroke="#2b2925" stroke-width=".8"/></svg><span><b>Maître d’œuvre :</b> ONDRA</span></li>
      <li><svg viewBox="0 0 10 10"><rect x="1.2" y="2" width="7.6" height="7" fill="none" stroke="#2b2925"/><path d="M1.2 4h7.6M3 1v2M7 1v2" stroke="#2b2925"/></svg><span><b>Livraison :</b> 2026</span></li>
    </ul>
    <span class="vrule" style="left:149px;top:233px;height:50px;background:var(--ink)"></span>

    <h3 class="abs h-a" style="left:165px;top:231px">LE RÔLE DE VERLO</h3>
    <ul class="abs list-a" style="left:165px;top:244px">
      <li><svg viewBox="0 0 10 10"><path d="M1.5 5.2l2.3 2.3L8.5 2.6" fill="none" stroke="#2b2925" stroke-width="1.5"/></svg>Conception de mobilier VARNIS sur-mesure</li>
      <li><svg viewBox="0 0 10 10"><path d="M1.5 5.2l2.3 2.3L8.5 2.6" fill="none" stroke="#2b2925" stroke-width="1.5"/></svg>Planification de pose par tranches</li>
      <li><svg viewBox="0 0 10 10"><path d="M1.5 5.2l2.3 2.3L8.5 2.6" fill="none" stroke="#2b2925" stroke-width="1.5"/></svg>Logistique de propreté « Zéro Poussière »</li>
      <li><svg viewBox="0 0 10 10"><path d="M1.5 5.2l2.3 2.3L8.5 2.6" fill="none" stroke="#2b2925" stroke-width="1.5"/></svg>Installation en mode « Discret »</li>
    </ul>
    <span class="rule-a" style="top:292px"></span>

    <h3 class="abs h-a" style="left:15px;top:296px">PRODUITS VERLO</h3>
    <div class="photo product-a photo-basin" style="left:15px" role="img" aria-label="Photo de la vasque ORVA KV310 avec robinet"></div>
    <div class="photo product-a photo-support" style="left:112px" role="img" aria-label="Photo du support VARNISOL sur-mesure en atelier"></div>
    <div class="photo product-a photo-mirror" style="left:208px" role="img" aria-label="Photo du miroir sur mesure"></div>
    <p class="product-label-a" style="left:15px">Vasque ORVA KV310</p>
    <p class="product-label-a" style="left:112px">Support VARNISOL<br>sur-mesure</p>
    <p class="product-label-a" style="left:208px">Miroir<br>sur mesure</p>
    <span class="rule-a" style="top:399px"></span>

    <p class="abs foot-a" style="left:15px;top:410px">Des solutions durables<br>pour les lieux de vie</p>
    <div class="abs brand-a" style="left:200px;top:407px;font-size:12px">Verlo.</div>
    <span class="vrule" style="left:253px;top:406px;height:21px;background:var(--ink)"></span>
    <p class="abs foot-tags-a" style="left:261px;top:408px">Concevoir<br>fabriquer<br>installer<br>durablement</p>
  </article>
</section>

<!-- ===== Spread B ===== -->
<section class="spread-b">
  <article class="page cover-b">
    <div class="photo photo-washroom" style="left:0;top:0;width:201px;height:100%" role="img" aria-label="Photo du bloc sanitaire : plan vasque blanc, meubles bois, mur vert et miroir"></div>
    <p class="abs kicker-b" style="left:13px;top:399px;color:var(--white);font-size:4.4px;line-height:9.5px;letter-spacing:2px">Espaces<br>durables<br>pour demain</p>
    <span class="hair" style="left:13px;top:431px;width:10px;background:var(--white)"></span>

    <div class="abs brand-b" style="left:218px;top:23px;font-size:13px;letter-spacing:6.5px">Norvi</div>
    <span class="hair" style="left:218px;top:76px;width:17px;background:var(--ink)"></span>
    <p class="abs project-b" style="left:218px;top:95px">PROJET</p>
    <h1 class="abs name-b" style="left:218px;top:108px">DELORME</h1>
    <p class="abs sub-b" style="left:218px;top:150px">L’ART DE L’AGILITÉ :<br>RÉNOVATION SANITAIRE<br>EN SITE OCCUPÉ</p>
    <span class="hair" style="left:218px;top:417px;width:17px;background:var(--ink)"></span>
    <p class="abs kicker-b" style="left:218px;top:428px;font-size:4.8px;font-weight:600;letter-spacing:1.6px;color:var(--ink)">norvi.fr</p>
  </article>

  <article class="page inner-b">
    <span class="hair" style="left:17px;top:16px;width:13px;background:var(--ink)"></span>
    <p class="abs kicker-b" style="right:14px;top:14px">Projet Delorme</p>
    <h2 class="title-b"><strong>Projet Delorme :</strong> quand la performance<br>s’adapte à la continuité de service</h2>

    <div class="photo photo-washroom" style="left:17px;top:72px;width:231px;height:113px" role="img" aria-label="Photo d’ensemble du plan vasque sous le grand miroir"></div>
    <p class="abs side-b" style="left:259px;top:87px">Fonctionnalité<br>esthétique<br>durabilité</p>
    <span class="hair" style="left:259px;top:118px;width:10px"></span>
    <p class="abs side-b" style="left:259px;top:126px">Des espaces<br>au service<br>des usagers</p>
    <span class="hair" style="left:259px;top:156px;width:10px"></span>

    <div class="photo photo-washroom" style="left:17px;top:189px;width:110px;height:85px" role="img" aria-label="Photo du sèche-mains au mur vert au-dessus d’une vasque"></div>
    <div class="photo photo-basin" style="left:131px;top:189px;width:99px;height:85px" role="img" aria-label="Photo rapprochée du robinet et de la vasque blanche"></div>
    <div class="tile-b"><p>Des<br>solutions<br>sur mesure<br>pour des lieux<br>qui comptent</p><span class="hair" style="left:9px;top:62px;width:9px;background:var(--paper-b)"></span></div>

    <h3 class="abs h-b" style="left:17px;top:290px">Données clé</h3>
    <span class="short-rule" style="left:17px;top:301px"></span>
    <p class="data-b" style="left:17px;top:312px"><b>Lieu :</b><br>12 Avenue Delorme, Paris 17e</p>
    <p class="data-b" style="left:17px;top:335px"><b>Maître d’ouvrage :</b><br>Banque Astrelle</p>
    <p class="data-b" style="left:17px;top:358px"><b>Maître d’œuvre :</b><br>ONDRA</p>
    <p class="data-b" style="left:17px;top:381px"><b>Livraison :</b><br>2026</p>
    <span class="vrule" style="left:106px;top:290px;height:118px"></span>

    <h3 class="abs h-b" style="left:115px;top:290px">Le rôle de Norvi</h3>
    <span class="short-rule" style="left:115px;top:301px"></span>
    <p class="role-b" style="left:115px;top:311px"><span>Conception de mobilier VARNIS<br>sur-mesure</span></p>
    <p class="role-b" style="left:115px;top:337px"><span>Planification de pose par tranches</span></p>
    <p class="role-b" style="left:115px;top:354px"><span>Logistique de propreté<br>« Zéro Poussière »</span></p>
    <p class="role-b" style="left:115px;top:380px"><span>Installation en mode « Discret »</span></p>
    <span class="vrule" style="left:217px;top:290px;height:118px"></span>

    <h3 class="abs h-b" style="left:226px;top:290px">Produits Norvi</h3>
    <span class="short-rule" style="left:226px;top:301px"></span>
    <div class="swatch-b photo-basin" style="top:307px" role="img" aria-label="Vignette de la vasque ORVA KV310"></div>
    <div class="swatch-b" style="top:341px;background:linear-gradient(160deg,#e9e7e3 0%,#e9e7e3 35%,#8b5a32 36%,#7a4f2c 100%)" role="img" aria-label="Vignette du support VARNISOL en bois"></div>
    <div class="swatch-b" style="top:376px;background:linear-gradient(90deg,#56683f 0%,#56683f 58%,#eeeeec 59%,#dcdcd8 100%)" role="img" aria-label="Vignette du miroir sur mesure devant le mur vert"></div>
    <p class="swatch-label-b" style="top:319px">Vasque<br>ORVA KV310</p>
    <p class="swatch-label-b" style="top:353px">Support VARNISOL<br>sur-mesure</p>
    <p class="swatch-label-b" style="top:389px">Miroir<br>sur mesure</p>

    <div class="abs brand-b" style="left:17px;top:425px;font-size:11px;letter-spacing:5px">Norvi</div>
    <span class="hair" style="left:96px;top:433px;width:100px;background:var(--rule)"></span>
    <p class="abs kicker-b" style="right:14px;top:431px">Espaces durables pour demain</p>
  </article>
</section>

</body>
</html>
```